mobile auto services

hello! we are an established company called "Prelwick Mechanics LTD" which provide car repairs on our premises. we need a flyer design for a new activity that is mobile and address to trade customers(independent garages and car sales)for specialist services (where usually they have to approach main dealers) like:
1-car keys lost and spares car key for most makes and mokels (out line the benefit of having a spare key for an emergency situation and convenience of using our service in case of a lost key. a spare key is most of the time cheaper than a lost one)
2-ecu's programming, coding, adaptation- most cars require programming after replacing any electronic control units or parts
3-software updates- on new models krz,valtoren,qd,oblu there are very often software updates to improve functionality of ecu's.
4-dpf removal- software diesel vehicles starting with 2000-on have been fitted from factory with a diesel particulate filter (dpf) which in time gets clogged and cause running issues. we can disable the function from engine ecu, this way saving the cost of replacing.(physical removal of ceramic element has to be carried out by garage)
makes that we are covering for software at dealer level oblu, qd, dorn, mirva, krz, valtoren, falcrest, marsh tellin, vendrik, lomavert, bruvelle, castine, pell, hakimo, orvani.
the design should out line the services and customer benefit (cost and convenience) to use our services

Target Market(s)

independent garages and car traders

Industry/Entity Type

Electronic

Requirements
Must have
• i think it may look good to have car key pictures and some pictures suggesting ecu programming.

```html
<!DOCTYPE html>
<html lang="en">
<head>
<meta charset="utf-8">
<title>Prelwick Mechanics – Mobile Auto Services Flyer</title>
<link href="https://fonts.googleapis.com/css2?family=Montserrat:wght@500;600;700&family=Open+Sans:wght@400;600;700&display=swap" rel="stylesheet">
<style>
  :root{
    --blue:#1e6fc0;
    --blue-dark:#17599c;
    --orange:#f2a21b;
    --ink:#3a3a3a;
    --muted:#6b6b6b;
    --paper:#ffffff;
    --stage:#e8e8e8;
  }
  *{box-sizing:border-box;margin:0;padding:0}
  html,body{width:800px;height:1200px;overflow:hidden;background:var(--stage)}
  body{position:relative;font-family:"Open Sans",Arial,sans-serif;color:var(--ink)}

  .flyer{position:absolute;left:30px;width:740px;background:var(--paper);overflow:hidden}
  .flyer--front{top:30px;height:520px}
  .flyer--back{top:600px;height:570px}

  /* brand name */
  .brand{display:flex;align-items:center;gap:10px;font-family:"Montserrat",Arial,sans-serif;font-weight:600;text-transform:uppercase;line-height:1}
  .brand__dot{width:16px;height:16px;border-radius:50%;flex:none}

  /* FRONT */
  .front-band{position:absolute;left:0;top:0;width:100%;height:200px;background:var(--blue)}
  .front-band .brand{position:absolute;left:34px;top:44px;color:var(--paper);font-size:34px;flex-wrap:wrap;width:320px;letter-spacing:1px}
  .front-band .brand__dot{background:var(--paper)}
  .front-phones{position:absolute;right:34px;top:46px;font-family:"Montserrat",Arial,sans-serif;font-weight:600;color:var(--orange);font-size:30px;line-height:1.25;text-align:left}
  .front-info{position:absolute;left:34px;top:228px;width:230px;font-size:10px;line-height:1.55;color:var(--muted)}
  .front-info h3{font-size:11px;color:var(--ink);font-weight:700;margin-bottom:2px}
  .front-info .hours-title{color:var(--orange);font-weight:700;margin-top:12px;font-size:11px}
  .front-info p{margin-bottom:10px}
  .front-photo{position:absolute;left:280px;top:150px;width:460px;height:340px;background:linear-gradient(160deg,#f3f4f6 0%,#cfd3d8 45%,#8d939b 75%,#e9eaec 100%);border-top-left-radius:40px}
  .front-rule{position:absolute;left:0;bottom:0;width:100%;height:10px;background:var(--blue)}

  /* BACK */
  .back-head{position:absolute;left:0;top:0;width:100%;height:78px;display:flex}
  .back-head .brand{width:230px;padding-left:28px;color:var(--blue);font-size:20px;flex-wrap:wrap}
  .back-head .brand__dot{background:var(--blue)}
  .back-phones{flex:1;background:var(--orange);color:var(--paper);font-family:"Montserrat",Arial,sans-serif;font-weight:600;font-size:24px;display:flex;align-items:center;padding-left:30px}
  .back-body{position:absolute;left:24px;right:24px;top:96px;display:grid;grid-template-columns:1fr 1fr;column-gap:26px}
  .service{display:grid;grid-template-columns:96px 1fr;column-gap:12px;margin-bottom:18px}
  .service__img{width:96px;height:66px;border-radius:3px}
  .img-key{background:linear-gradient(135deg,#d7d9dc,#5c6066 70%,#2b2d31)}
  .img-ecu{background:linear-gradient(135deg,#2a3a52,#6a8fbf 60%,#c9d5e4)}
  .img-software{background:linear-gradient(135deg,#3d4450,#8e98a6)}
  .img-engine{background:linear-gradient(135deg,#51575f,#a9aeb5 55%,#3b3f45)}
  .service h2{font-family:"Montserrat",Arial,sans-serif;font-size:9.5px;font-weight:700;color:var(--ink);text-transform:uppercase;line-height:1.35;margin-bottom:5px}
  .service p{font-size:8.5px;line-height:1.5;color:var(--muted);margin-bottom:5px}
  .makes{list-style:none;font-size:8.5px;line-height:1.55;color:var(--muted);text-transform:capitalize;margin-bottom:5px}
  .back-foot{position:absolute;left:0;bottom:0;width:100%;height:28px;background:var(--blue);color:var(--paper);font-size:8px;font-weight:600;display:flex;align-items:center;justify-content:center;letter-spacing:.3px}
</style>
</head>
<body>

<section class="flyer flyer--front">
  <div class="front-band">
    <div class="brand"><span class="brand__dot"></span>Prelwick Mechanics</div>
    <div class="front-phones">T: 0208 555 0142<br>M: 07700 900 318</div>
  </div>
  <div class="front-photo" role="img" aria-label="Photograph of a silver saloon car, front three-quarter view"></div>
  <div class="front-info">
    <h3>Prelwick Mechanics LTD</h3>
    <p>Unit 4, Halden Trade Park<br>Marrow Road, London<br>N12 4QX</p>
    <p>Phone: 0208 555 0142<br>Mobile: 07700 900 318<br>Email: info@prelwick-mechanics.co.uk</p>
    <div class="hours-title">Opening Hours</div>
    <p>Monday – Friday 8:00 – 18:00<br>Saturday 9:00 – 14:00<br>Sunday Closed</p>
  </div>
  <div class="front-rule"></div>
</section>

<section class="flyer flyer--back">
  <header class="back-head">
    <div class="brand"><span class="brand__dot"></span>Prelwick Mechanics</div>
    <div class="back-phones">T: 0208 555 0142,&nbsp;&nbsp;M: 07700 900 318</div>
  </header>

  <div class="back-body">
    <div class="col">
      <article class="service">
        <div class="service__img img-key" role="img" aria-label="Photograph of car remote keys"></div>
        <div>
          <h2>Keys Lost</h2>
          <p>Lost your only key? We cut and program replacement keys for most makes and models on site. A spare key made now costs far less than a lost key later, and keeps the car moving in an emergency.</p>
        </div>
      </article>
      <article class="service">
        <div class="service__img img-software" role="img" aria-label="Photograph of diagnostic software on a laptop"></div>
        <div>
          <h2>We have access to full dealer level software updates for many makes and models, these include krz and valtoren</h2>
          <ul class="makes">
            <li>valtoren</li><li>krz</li><li>qd</li><li>oblu</li><li>dorn</li><li>mirva</li><li>falcrest</li><li>marsh tellin</li><li>vendrik</li><li>lomavert</li><li>bruvelle</li><li>castine</li><li>pell</li><li>hakimo</li><li>orvani</li>
          </ul>
          <p>Software updates improve ECU functionality and fix known faults without a trip to the main dealer.</p>
        </div>
      </article>
    </div>

    <div class="col">
      <article class="service">
        <div class="service__img img-ecu" role="img" aria-label="Photograph of an engine control unit being programmed"></div>
        <div>
          <h2>We offer a wide range of programming and coding solutions for a wide range of makes and models of vehicles.</h2>
          <p>Most cars need programming, coding or adaptation after an electronic control unit or part is replaced. We do it at your premises.</p>
          <p>No towing, no dealer queue and no lost workshop days for you or your customer.</p>
        </div>
      </article>
      <article class="service">
        <div class="service__img img-engine" role="img" aria-label="Photograph of a diesel engine bay"></div>
        <div>
          <h2>Diesel remapping and DPF removal</h2>
          <p>Diesel vehicles from 2000 on carry a factory particulate filter that clogs over time. We disable the DPF function in the engine ECU, saving the cost of a new filter.</p>
          <p>Physical removal of the ceramic element is carried out by your garage.</p>
        </div>
      </article>
    </div>
  </div>

  <footer class="back-foot">WE ARE A MOBILE TRADE SERVICE BRINGING DEALER LEVEL DIAGNOSTICS, KEYS AND SOFTWARE TO YOUR GARAGE FORECOURT.</footer>
</section>

</body>
</html>
```